Sleek, Professional Business Card Design Needed

Business Cards - Logo Attached.

We are a solar consulting company. We are national and want our cards to represent the professional high quality products that we offer.

Industry/Entity Type

Business

Contact Information for Business Card

n/a

Requirements
Must have
• Design
• Name
• Position
• Number
• Email
• Address
Should not have
• Not be too crowded

```html
<!DOCTYPE html>
<html lang="en">
<head>
<meta charset="utf-8">
<title>Bright Field Energy – Business Card</title>
<link href="https://fonts.googleapis.com/css2?family=Roboto+Condensed:wght@700&family=Roboto:wght@400;500&display=swap" rel="stylesheet">
<style>
  :root {
    --stage: #2a2a2b;
    --card: #232425;
    --blue: #1ea3dd;
    --green: #b4d234;
    --white: #f2f2f2;
    --divider: #cfcfcf;
  }
  * { margin: 0; padding: 0; box-sizing: border-box; }
  html, body { width: 1200px; height: 900px; overflow: hidden; }
  body {
    background: var(--stage);
    font-family: "Roboto", Arial, sans-serif;
    display: flex;
    flex-direction: column;
    align-items: center;
    justify-content: center;
    gap: 34px;
  }
  .card {
    width: 700px;
    height: 390px;
    background: var(--card);
    position: relative;
    box-shadow: 0 14px 30px rgba(0,0,0,.45);
  }
  /* Front */
  .card--front {
    display: flex;
    flex-direction: column;
    align-items: center;
    justify-content: center;
    gap: 34px;
  }
  .brand {
    display: flex;
    align-items: center;
    gap: 16px;
  }
  .brand__name {
    font-family: "Roboto Condensed", Arial, sans-serif;
    font-weight: 700;
    font-size: 40px;
    letter-spacing: 1px;
    color: var(--blue);
    text-transform: uppercase;
  }
  .front__web {
    color: var(--white);
    font-size: 16px;
    letter-spacing: 3px;
  }
  /* Back */
  .identity {
    position: absolute;
    left: 110px;
    top: 126px;
    width: 220px;
    text-align: right;
  }
  .identity__name {
    font-family: "Roboto Condensed", Arial, sans-serif;
    font-weight: 700;
    font-size: 38px;
    color: var(--blue);
    line-height: 1;
  }
  .identity__role {
    font-family: "Roboto Condensed", Arial, sans-serif;
    font-weight: 700;
    font-size: 18px;
    color: var(--green);
    margin-top: 6px;
  }
  .divider {
    position: absolute;
    left: 355px;
    top: 112px;
    width: 2px;
    height: 90px;
    background: linear-gradient(to bottom, transparent, var(--divider), transparent);
  }
  .contacts {
    position: absolute;
    left: 380px;
    top: 132px;
    list-style: none;
  }
  .contacts li {
    display: flex;
    align-items: center;
    gap: 10px;
    color: var(--white);
    font-size: 17px;
    font-weight: 500;
    line-height: 24px;
  }
  .icon { width: 15px; height: 15px; flex: none; }
  .address {
    position: absolute;
    left: 110px;
    bottom: 70px;
    display: flex;
    align-items: center;
    gap: 6px;
    color: var(--white);
    font-size: 17px;
    font-weight: 500;
  }
</style>
</head>
<body>
  <section class="card card--front">
    <div class="brand">
      <svg width="34" height="34" viewBox="0 0 34 34" aria-hidden="true"><circle cx="17" cy="17" r="15" fill="none" stroke="#1ea3dd" stroke-width="4"/></svg>
      <span class="brand__name">Bright Field Energy</span>
    </div>
    <p class="front__web">www.brightfieldenergy.com</p>
  </section>

  <section class="card card--back">
    <div class="identity">
      <h1 class="identity__name">DANIEL REYES</h1>
      <p class="identity__role">CEO/FOUNDER</p>
    </div>
    <div class="divider"></div>
    <ul class="contacts">
      <li>
        <svg class="icon" viewBox="0 0 16 16" aria-hidden="true"><path fill="#1ea3dd" d="M3.6 1.2l2.3 2.6-1.3 1.8c.9 2 2.6 3.7 4.6 4.6l1.8-1.3 2.6 2.3-1.4 2.3C6.9 14.5 1.5 9.1 1.3 3.1z"/></svg>
        555 014 2738
      </li>
      <li>
        <svg class="icon" viewBox="0 0 16 16" aria-hidden="true"><rect x="1" y="3" width="14" height="10" rx="1" fill="#1ea3dd"/><path d="M1.5 3.8L8 9l6.5-5.2" fill="none" stroke="#232425" stroke-width="1.3"/></svg>
        name@brightfieldenergy.com
      </li>
      <li>
        <svg class="icon" viewBox="0 0 16 16" aria-hidden="true"><circle cx="8" cy="8" r="7" fill="#1ea3dd"/><path d="M1 8h14M8 1c-3 3.5-3 10.5 0 14M8 1c3 3.5 3 10.5 0 14" fill="none" stroke="#232425" stroke-width="1.1"/></svg>
        www.brightfieldenergy.com
      </li>
    </ul>
    <p class="address">
      <svg class="icon" viewBox="0 0 16 16" aria-hidden="true"><path fill="#1ea3dd" d="M8 .5a5 5 0 0 0-5 5c0 3.8 5 10 5 10s5-6.2 5-10a5 5 0 0 0-5-5zm0 7a2 2 0 1 1 0-4 2 2 0 0 1 0 4z"/></svg>
      4120 Larkspur Road, Juneau, Alaska 99801
    </p>
  </section>
</body>
</html>
```